Dubai Family protection infographic

We need to produce a way of attracting people to a life insurance and critical illness cover seminar. As this is a pretty dull subject for most people, so we need a cool way of getting people to read the invite/marketing collateral.

We're thinking some kind of colourful and attractive infographic that we can use on flyers and posters as well as online and as an emailer.

Content for the graphic is as bellow:

How much does it cost to replace Mum & Dad?

Mum = Chauffer, Cook, Laundry Service, Household Cleaner, Psychologist, Money Manager

Mums typically work a 94-hour week. At a rather paltry $12 per hour, that’s $4,888 per month – or $58,656 each year. (Source: wagelore.net)

Dad : The average Western Expat’s salary in the Gulf is $12,215 per month. That’s $146,580 each year. (Source: Palmcrest Ledger).

Did you know that the average age of critical illness claimants in the Middle East last year was just 48. Of these, 44% were for cancer while 41% were heart related.

The average age of a death claimant was just 50 years old.
(Source: Verenholt Assurance Group)

1 in 3 people will develop some form of cancer during their lifetime.

That’s 2.36 billion people globally.

And that’s equivalent to the population of China, USA, Brazil, Russia, Philippines, France, UK, South Africa and Italy combined.

Does your family have the resources to hand to cope if a tragedy happens to you?

What can you do to protect them and yourself?

Come to the UAE’s first national protection seminar to find out. Join us at Harbourline Riverside Sports Arena on June 19th at 19:00.

To pre-register, visit www.tovanmere.net/events or alternatively register on the door.

```html
<!DOCTYPE html>
<html lang="en">
<head>
<meta charset="utf-8">
<title>How much does it cost to replace Mum &amp; Dad?</title>
<link href="https://fonts.googleapis.com/css2?family=Arimo:wght@400;700&family=Tinos:wght@400;700&display=swap" rel="stylesheet">
<style>
:root{
  --pink:#e0457b;
  --pink-soft:#f07aa2;
  --plum:#8a3c78;
  --blue:#2a8fd0;
  --ink:#333;
  --grey:#7c7c7c;
  --panel:#e4e4e4;
  --band:#9a9a9a;
  --yellow:#ffe400;
  --cream:#fffbe0;
  --paper:#f5f5f5;
}
*{box-sizing:border-box;margin:0;padding:0}
html,body{width:802px;height:1200px;overflow:hidden}
body{background:var(--paper);font-family:"Arimo",Arial,sans-serif;color:var(--ink);position:relative}
.title{position:absolute;top:24px;left:0;width:802px;text-align:center;font-size:46px;font-weight:700;line-height:1.12;color:var(--pink)}
.title em{font-style:normal;color:var(--plum)}
.parents-art{position:absolute;left:270px;top:140px;width:262px;height:150px;border-radius:16px;background:linear-gradient(135deg,#f3c9a9,#e8b38f 50%,#c9d7e8)}
.mum-box{position:absolute;left:44px;top:160px;width:206px;padding:12px 14px;background:var(--pink-soft);color:#fff;font-size:17px;line-height:1.3;border-radius:6px}
.dad-box{position:absolute;left:548px;top:158px;width:220px;font-size:16px;line-height:1.3;color:#fff;background:var(--blue);padding:10px 12px;border-radius:6px}
.mum-note{position:absolute;left:100px;top:298px;width:602px;text-align:center;font-size:12px;color:var(--grey);line-height:1.4}
.facts{position:absolute;left:34px;top:360px;width:734px;height:374px;background:var(--panel);border-radius:22px}
.facts h2{text-align:center;margin-top:20px;font-size:44px;color:var(--ink)}
.facts .lead{text-align:center;margin:10px auto 0;width:600px;font-size:22px;line-height:1.3;color:var(--pink)}
.people-art{position:absolute;left:120px;top:180px;width:500px;height:66px;border-radius:33px;background:linear-gradient(90deg,#d8b899,#a8785a,#e0b894)}
.stat{position:absolute;top:256px;width:212px;height:92px;font-size:17px;font-weight:700;line-height:1.25;text-align:center;padding:6px}
.stat small{display:block;font-size:11px;font-weight:400;color:var(--grey)}
.stat-age{left:24px;background:var(--yellow)}
.stat-cancer{left:262px;background:var(--cream)}
.stat-billion{left:498px;font-size:20px;line-height:1.15;padding-top:2px}
.stat-billion b{color:var(--pink);font-size:40px}
.globe-art{position:absolute;left:66px;top:744px;width:70px;height:70px;border-radius:50%;background:radial-gradient(circle at 35% 35%,#bfe3f5,#3a8ec4)}
.equivalent{position:absolute;left:100px;top:751px;width:668px;height:56px;background:var(--band);color:#fff;font-size:17px;line-height:1.3;text-align:center;padding:7px 20px 0 60px;border-radius:0 28px 28px 0}
.call{position:absolute;left:0;top:830px;width:802px;height:240px;background:var(--yellow);font-family:"Tinos","Times New Roman",serif;text-align:center;color:var(--ink);padding-top:34px}
.call h3{font-size:34px;font-weight:400}
.call p{font-size:24px;margin-top:6px}
.call h3 + p{margin-bottom:30px}
.invite{position:absolute;left:0;top:1070px;width:802px;height:130px;background:#fff;font-family:"Tinos","Times New Roman",serif;text-align:center;font-size:19px;line-height:1.45;padding-top:20px;color:var(--ink)}
.invite p + p{margin-top:8px}
</style>
</head>
<body>
<h1 class="title">How much <em>does it cost</em><br>to replace Mum &amp; Dad?</h1>

<div class="parents-art" role="img" aria-label="Illustration of a mother and a father"></div>
<div class="mum-box"><b>Mum =</b> Chauffer, Cook, Laundry Service, Household Cleaner, Psychologist, Money Manager</div>
<div class="dad-box"><b>Dad</b>: The average Western Expat’s salary in the Gulf is $12,215 per month. That’s $146,580 each year. (Source: Palmcrest Ledger).</div>
<p class="mum-note">Mums typically work a 94-hour week.<br>At a rather paltry $12 per hour, that’s $4,888 per month – or $58,656 each year.<br>(Source: wagelore.net)</p>

<section class="facts">
  <h2>Did you know</h2>
  <p class="lead">that the average age of critical illness claimants in the Middle East last year was just 48. Of these, 44% were for cancer while 41% were heart related.</p>
  <div class="people-art" role="img" aria-label="Illustration of three people of different backgrounds"></div>
  <div class="stat stat-age">The average age of a death claimant was just 50 years old.<small>(Source: Verenholt Assurance Group)</small></div>
  <div class="stat stat-cancer">1 in 3 people will develop some form of cancer during their lifetime.</div>
  <div class="stat stat-billion">That’s <b>2.36</b> billion people globally.</div>
</section>

<div class="equivalent">And that’s equivalent to the population of China, USA, Brazil, Russia, Philippines, France, UK, South Africa and Italy combined.</div>
<div class="globe-art" role="img" aria-label="Illustration of a globe"></div>

<section class="call">
  <h3>Does your family</h3>
  <p>have the resources to hand to cope if a tragedy happens to you?</p>
  <h3>What can you do</h3>
  <p>to protect them and yourself?</p>
</section>

<section class="invite">
  <p>Come to the UAE’s first national protection seminar to find out.<br>Join us at <b>Harbourline Riverside Sports Arena on June 19th at 19:00.</b></p>
  <p>To pre-register, visit <b>www.tovanmere.net/events</b> or alternatively register on the door.</p>
</section>
</body>
</html>
```